Typographic word art illustration of life lessons

I've written out all the meaningful life lessons my parents have taught me and would like to give it to them for Christmas in the form of a typographic word art design. This will be a print project. I'd like the size of the design to be no larger than 11x17, no smaller than 8.5x11.
The text must be readable in the complete sentences provided.
The text can be displayed in multiple directions, as long as each sentence is readable.
The text itself should be arranged in an artistic and creative way. I'm not looking for text that is aligned in normal-looking rows with a an image watermark behind it.
Sentences may be included on the same row if it works with the design.
Font, Case and Text may be alternated to best suite your design. No grunge fonts, or small-size handwriting fonts, or anything that is difficult to read.
Text could fit into a shape or silhouette (ie: heart, tree, or anything that symbolizes family, life, love, etc.), or form an abstract design, or it can be justified to fit the whole page.
I'm not looking for anything super colorful. Black and white would work, or any standard color palette. The intended result is something they can hang on their wall.
Text is attached in a pdf. Minor tweaks to text is ok if necessary for formatting design, but in general, text should remain unedited.
I've also added some examples of the type of word art I had in mind.
Please help me make this gift into something beautiful and special!
Updates
I trimmed the text down significantly because all the designs seemed to crowded, and had to use fonts that were too small. Here is the revised text:
Don’t give up until you’ve given your all.
Don’t let people that hurt you occupy your mind.
Good people do bad things. Get over it.
Block bitterness from ever taking root in your heart.
Take every opportunity to express gratitude.
True brotherhood is forged out of loyalty and love.
There is no excuse for deceit.
Words matter.
Forgiveness is not optional.
Never make insincere apologies.
Worrying is a waste of time.
Choose your destiny by choosing your friends.
Marriage is a unified front. Make your spouse a priority.
Truth and grace are inseparable.
Humor disarms, softens and endears.
Selflessness is a lifestyle.
Whenever possible, give generously and anonymously.
Never apologize and give an excuse in the same sentence.
Faith must fuel the core of who you are.
The path to freedom begins with asking difficult questions.
Take advantage of every opportunity to educate yourself.
Be your spouse’s protector and advocate.
Radiate humility, vulnerability and love.
Give your finish line the ability to expand.

```html
<!DOCTYPE html>
<html lang="en">
<head>
<meta charset="utf-8">
<title>Life Lessons – Typographic Poster</title>
<link rel="stylesheet" href="https://fonts.googleapis.com/css2?family=Anton&family=Archivo+Black&family=Oswald:wght@300;400;700&display=swap">
<style>
  :root {
    --ink: #111111;
    --paper: #ffffff;
  }
  html, body {
    margin: 0;
    padding: 0;
    width: 776px;
    height: 1200px;
    overflow: hidden;
    background: var(--paper);
  }
  .poster {
    display: block;
    width: 776px;
    height: 1200px;
  }
  .poster text { fill: var(--ink); }
  .heavy { font-family: "Anton", "Oswald", sans-serif; }
  .wide  { font-family: "Archivo Black", "Arial Black", sans-serif; }
  .bold  { font-family: "Oswald", sans-serif; font-weight: 700; }
  .light { font-family: "Oswald", sans-serif; font-weight: 300; }
  .regular { font-family: "Oswald", sans-serif; font-weight: 400; }
  .kite-string { fill: none; stroke: var(--ink); stroke-width: 1.2; }
  .arrow-head, .ground, .couple { fill: var(--ink); }
</style>
</head>
<body>
<svg class="poster" viewBox="0 0 776 1200" xmlns="http://www.w3.org/2000/svg">
  <g class="word-kite">
    <text class="heavy" x="150" y="122" font-size="45" textLength="130" lengthAdjust="spacingAndGlyphs">DON’T</text>
    <text class="light" x="283" y="120" font-size="24" textLength="67" lengthAdjust="spacingAndGlyphs">GIVE UP</text>
    <text class="bold" x="123" y="146" font-size="20" textLength="279" lengthAdjust="spacingAndGlyphs">UNTIL YOU’VE GIVEN YOUR ALL.</text>

    <text class="regular" x="92" y="166" font-size="12" textLength="121" lengthAdjust="spacingAndGlyphs">DON’T LET PEOPLE THAT</text>
    <text class="regular" x="65" y="185" font-size="14" textLength="150" lengthAdjust="spacingAndGlyphs">OCCUPY YOUR MIND.</text>
    <text class="light" x="221" y="190" font-size="44" textLength="191" lengthAdjust="spacingAndGlyphs">HURT YOU</text>

    <text class="heavy" transform="translate(82,245) rotate(-90)" font-size="30" textLength="47" lengthAdjust="spacingAndGlyphs">GOOD</text>
    <text class="regular" x="87" y="222" font-size="28" textLength="108" lengthAdjust="spacingAndGlyphs">PEOPLE</text>
    <text class="regular" x="87" y="250" font-size="28" textLength="108" lengthAdjust="spacingAndGlyphs">DO BAD</text>
    <text class="heavy" x="200" y="250" font-size="60" textLength="228" lengthAdjust="spacingAndGlyphs">THINGS.</text>

    <text class="heavy" x="42" y="296" font-size="34" textLength="188" lengthAdjust="spacingAndGlyphs">GET OVER IT.</text>
    <text class="regular" x="236" y="281" font-size="17" textLength="187" lengthAdjust="spacingAndGlyphs">BLOCK BITTERNESS FROM</text>
    <text class="regular" x="236" y="300" font-size="17" textLength="200" lengthAdjust="spacingAndGlyphs">EVER TAKING ROOT IN YOUR</text>

    <text class="wide" x="37" y="370" font-size="90" textLength="418" lengthAdjust="spacingAndGlyphs">HEART.</text>
    <text class="bold" x="465" y="350" font-size="17" textLength="155" lengthAdjust="spacingAndGlyphs">TRUE BROTHERHOOD</text>
    <text class="bold" x="465" y="370" font-size="17" textLength="195" lengthAdjust="spacingAndGlyphs">IS FORGED OUT OF LOYALTY AND</text>

    <text class="regular" x="40" y="398" font-size="20" textLength="342" lengthAdjust="spacingAndGlyphs">TAKE EVERY OPPORTUNITY TO EXPRESS</text>
    <text class="light" x="395" y="418" font-size="50" textLength="130" lengthAdjust="spacingAndGlyphs">LOVE.</text>
    <text class="regular" x="535" y="398" font-size="22" textLength="135" lengthAdjust="spacingAndGlyphs">THERE IS NO</text>
    <text class="regular" x="535" y="418" font-size="16" textLength="130" lengthAdjust="spacingAndGlyphs">EXCUSE FOR DECEIT.</text>

    <text class="heavy" x="50" y="458" font-size="59" textLength="335" lengthAdjust="spacingAndGlyphs">GRATITUDE.</text>
    <text class="regular" x="395" y="460" font-size="38" textLength="327" lengthAdjust="spacingAndGlyphs">WORDS MATTER.</text>

    <text class="bold" x="53" y="482" font-size="14" textLength="100" lengthAdjust="spacingAndGlyphs">FORGIVENESS IS</text>
    <text class="bold" x="55" y="500" font-size="18" textLength="97" lengthAdjust="spacingAndGlyphs">OPTIONAL.</text>
    <text class="heavy" transform="translate(172,498) rotate(-90)" font-size="18" textLength="30" lengthAdjust="spacingAndGlyphs">NOT</text>
    <text class="regular" x="188" y="481" font-size="15" textLength="69" lengthAdjust="spacingAndGlyphs">NEVER MAKE</text>
    <text class="regular" x="188" y="500" font-size="15" textLength="77" lengthAdjust="spacingAndGlyphs">INSINCERE</text>
    <text class="light" x="288" y="502" font-size="34" textLength="187" lengthAdjust="spacingAndGlyphs">APOLOGIES.</text>
    <text class="regular" x="480" y="484" font-size="18" textLength="258" lengthAdjust="spacingAndGlyphs">WORRYING IS A WASTE OF TIME.</text>
    <text class="regular" x="481" y="502" font-size="11" textLength="257" lengthAdjust="spacingAndGlyphs">CHOOSE YOUR DESTINY BY CHOOSING YOUR FRIENDS.</text>

    <text class="heavy" x="60" y="549" font-size="44" textLength="182" lengthAdjust="spacingAndGlyphs">MARRIAGE</text>
    <text class="regular" x="250" y="527" font-size="14" textLength="76" lengthAdjust="spacingAndGlyphs">IS A UNIFIED</text>
    <text class="regular" x="250" y="549" font-size="22" textLength="76" lengthAdjust="spacingAndGlyphs">FRONT.</text>
    <text class="bold" x="332" y="528" font-size="17" textLength="48" lengthAdjust="spacingAndGlyphs">MAKE</text>
    <text class="bold" x="332" y="549" font-size="17" textLength="48" lengthAdjust="spacingAndGlyphs">YOUR</text>
    <text class="heavy" x="383" y="540" font-size="36" textLength="124" lengthAdjust="spacingAndGlyphs">SPOUSE</text>
    <text class="bold" x="422" y="552" font-size="10" textLength="86" lengthAdjust="spacingAndGlyphs">A PRIORITY.</text>
    <text class="light" x="518" y="530" font-size="24" textLength="130" lengthAdjust="spacingAndGlyphs">TRUTH AND</text>
    <text class="regular" x="522" y="551" font-size="17" textLength="123" lengthAdjust="spacingAndGlyphs">ARE INSEPARABLE.</text>
    <text class="heavy" x="652" y="550" font-size="44" textLength="95" lengthAdjust="spacingAndGlyphs">GRACE</text>

    <text class="regular" x="72" y="572" font-size="16" textLength="126" lengthAdjust="spacingAndGlyphs">HUMOR DISARMS,</text>
    <text class="regular" x="72" y="586" font-size="12" textLength="131" lengthAdjust="spacingAndGlyphs">SOFTENS AND ENDEARS.</text>
    <text class="regular" x="208" y="569" font-size="11" textLength="92" lengthAdjust="spacingAndGlyphs">SELFLESSNESS IS A</text>
    <text class="regular" x="207" y="588" font-size="20" textLength="97" lengthAdjust="spacingAndGlyphs">LIFESTYLE.</text>
    <text class="bold" x="318" y="575" font-size="13" textLength="147" lengthAdjust="spacingAndGlyphs">WHENEVER POSSIBLE,</text>
    <text class="bold" x="318" y="589" font-size="13" textLength="147" lengthAdjust="spacingAndGlyphs">GIVE GENEROUSLY AND</text>
    <text class="heavy" x="472" y="591" font-size="36" textLength="265" lengthAdjust="spacingAndGlyphs">ANONYMOUSLY.</text>

    <text class="heavy" x="77" y="639" font-size="48" textLength="148" lengthAdjust="spacingAndGlyphs">NEVER</text>
    <text class="regular" x="234" y="619" font-size="22" textLength="271" lengthAdjust="spacingAndGlyphs">APOLOGIZE AND GIVE AN EXCUSE</text>
    <text class="regular" x="234" y="641" font-size="22" textLength="266" lengthAdjust="spacingAndGlyphs">IN THE SAME SENTENCE.</text>
    <text class="heavy" transform="translate(528,643) rotate(-90)" font-size="20" textLength="43" lengthAdjust="spacingAndGlyphs">FAITH</text>
    <text class="bold" x="532" y="619" font-size="22" textLength="200" lengthAdjust="spacingAndGlyphs">MUST FUEL THE CORE</text>
    <text class="bold" x="532" y="641" font-size="22" textLength="173" lengthAdjust="spacingAndGlyphs">OF WHO YOU ARE.</text>

    <text class="bold" x="80" y="663" font-size="13" textLength="73" lengthAdjust="spacingAndGlyphs">THE PATH TO</text>
    <text class="bold" x="80" y="677" font-size="13" textLength="73" lengthAdjust="spacingAndGlyphs">BEGINS WITH</text>
    <text class="heavy" x="158" y="677" font-size="32" textLength="147" lengthAdjust="spacingAndGlyphs">FREEDOM</text>
    <text class="regular" x="317" y="660" font-size="13" textLength="155" lengthAdjust="spacingAndGlyphs">TAKE ADVANTAGE OF EVERY</text>
    <text class="regular" x="317" y="676" font-size="13" textLength="155" lengthAdjust="spacingAndGlyphs">OPPORTUNITY TO EDUCATE</text>
    <text class="wide" x="478" y="677" font-size="30" textLength="225" lengthAdjust="spacingAndGlyphs">YOURSELF.</text>

    <text class="regular" x="80" y="700" font-size="20" textLength="151" lengthAdjust="spacingAndGlyphs">BE YOUR SPOUSE’S</text>
    <text class="regular" x="80" y="720" font-size="20" textLength="135" lengthAdjust="spacingAndGlyphs">PROTECTOR AND</text>
    <text class="heavy" x="232" y="720" font-size="45" textLength="246" lengthAdjust="spacingAndGlyphs">ADVOCATE.</text>
    <text class="heavy" transform="translate(500,746) rotate(-90)" font-size="20" textLength="58" lengthAdjust="spacingAndGlyphs">RADIATE</text>
    <text class="regular" x="503" y="713" font-size="24" textLength="137" lengthAdjust="spacingAndGlyphs">HUMILITY,</text>
    <text class="regular" x="503" y="727" font-size="14" textLength="125" lengthAdjust="spacingAndGlyphs">VULNERABILITY</text>
    <text class="regular" x="503" y="742" font-size="14" textLength="94" lengthAdjust="spacingAndGlyphs">AND LOVE.</text>

    <text class="wide" x="75" y="745" font-size="19" textLength="400" lengthAdjust="spacingAndGlyphs">GIVE YOUR FINISH LINE THE</text>
    <text class="wide" x="75" y="765" font-size="17" textLength="105" lengthAdjust="spacingAndGlyphs">ABILITY TO</text>
    <text class="wide" x="66" y="784" font-size="11" textLength="61" lengthAdjust="spacingAndGlyphs">EXPAND.</text>
  </g>

  <g class="kite-line">
    <polygon class="arrow-head" points="68,788 60,802 74,800"/>
    <path class="kite-string" d="M67,800 C60,850 90,880 200,888 C330,896 470,880 590,910 C650,925 678,960 683,1000 C688,1040 684,1060 692,1088"/>
  </g>

  <rect class="couple" x="580" y="943" width="196" height="222" role="img" aria-label="Silhouette of a couple holding a kite string together"/>

  <g class="footnote">
    <text class="regular" x="75" y="1117" font-size="9" textLength="250" lengthAdjust="spacingAndGlyphs">NEED TEXT FOR BALANCE THE DESIGN SOFTENS AND ENDEARS.</text>
    <text class="regular" x="75" y="1131" font-size="9" textLength="236" lengthAdjust="spacingAndGlyphs">SELFLESSNESS IS A LIFESTYLE. WHENEVER POSSIBLE, GIVE</text>
  </g>

  <path class="ground" d="M0,1152 C200,1146 500,1148 776,1136 L776,1200 L0,1200 Z"/>
</svg>
</body>
</html>
```